Structural Engineering Business Card

Veltrow Drafts does residential house plans for clients in Central Florida. Would like simple but elegant business card that is appropriate for a house plan engineering company. Prefer black business card with black/white them but open to other shades of blue. I uploaded a sample card that I came across that looked good but please come up with your own creative designs.

Contact Information for Business Card

Name, Title, Phone, Email, Address, website

```html
<!DOCTYPE html>
<html lang="en">
<head>
<meta charset="utf-8">
<title>Veltrow Drafts — Business Card</title>
<link href="https://fonts.googleapis.com/css2?family=Roboto:wght@400;700;900&display=swap" rel="stylesheet">
<style>
  :root {
    --backdrop: #d8d8d5;
    --card: #ffffff;
    --ink: #111111;
    --ink-soft: #3a3a3a;
    --edge: #000000;
  }
  * { box-sizing: border-box; margin: 0; padding: 0; }
  html, body {
    width: 1200px; height: 801px; overflow: hidden;
    background: var(--backdrop);
    font-family: "Roboto", Arial, sans-serif;
    color: var(--ink);
  }
  .canvas {
    position: relative; width: 1200px; height: 801px;
    display: flex; align-items: center; justify-content: center; gap: 48px;
  }
  .card {
    position: relative;
    width: 540px; height: 309px;
    background: var(--card);
    border-bottom: 3px solid var(--edge);
    box-shadow: 0 14px 30px rgba(0,0,0,0.18);
  }
  .wordmark {
    display: flex; align-items: center; gap: 10px;
    font-weight: 900; text-transform: uppercase;
    color: var(--ink); line-height: 1; letter-spacing: 0.01em;
  }
  .wordmark__square { background: var(--ink); flex: none; }

  /* Front */
  .card--front .wordmark { position: absolute; left: 36px; top: 40px; font-size: 30px; }
  .card--front .wordmark__square { width: 22px; height: 22px; }
  .holder { position: absolute; right: 36px; top: 40px; text-align: right; }
  .holder__name { font-weight: 700; font-size: 19px; letter-spacing: 0.02em; }
  .holder__title { font-size: 12px; color: var(--ink-soft); margin-top: 3px; }
  .contact { position: absolute; left: 36px; bottom: 32px; font-size: 12.5px; color: var(--ink-soft); }
  .contact__address { line-height: 1.45; margin-bottom: 16px; }
  .contact__list { list-style: none; }
  .contact__item { display: flex; align-items: center; gap: 8px; line-height: 1.55; }
  .contact__icon { width: 12px; height: 12px; fill: var(--ink); flex: none; }

  /* Back */
  .card--back { display: flex; align-items: center; justify-content: center; }
  .card--back .wordmark { font-size: 44px; gap: 14px; }
  .card--back .wordmark__square { width: 32px; height: 32px; }
</style>
</head>
<body>
<main class="canvas">
  <section class="card card--front" aria-label="Card front">
    <div class="wordmark"><span class="wordmark__square"></span>Veltrow Drafts</div>
    <div class="holder">
      <p class="holder__name">DORIAN KESSEL</p>
      <p class="holder__title">Managing Director</p>
    </div>
    <div class="contact">
      <p class="contact__address">Your address, City<br>State, Zip 1234</p>
      <ul class="contact__list">
        <li class="contact__item">
          <svg class="contact__icon" viewBox="0 0 24 24"><path d="M6.6 10.8a15 15 0 0 0 6.6 6.6l2.2-2.2a1 1 0 0 1 1-.25 11.4 11.4 0 0 0 3.6.57 1 1 0 0 1 1 1V20a1 1 0 0 1-1 1A17 17 0 0 1 3 4a1 1 0 0 1 1-1h3.5a1 1 0 0 1 1 1c0 1.25.2 2.45.57 3.57a1 1 0 0 1-.25 1z"/></svg>
          123 456 789
        </li>
        <li class="contact__item">
          <svg class="contact__icon" viewBox="0 0 24 24"><path d="M2 5h20v14H2z M2 5l10 8 10-8" /></svg>
          info@yourgmail.com
        </li>
        <li class="contact__item">
          <svg class="contact__icon" viewBox="0 0 24 24"><circle cx="12" cy="12" r="10"/></svg>
          www.yourwebsite.com
        </li>
      </ul>
    </div>
  </section>

  <section class="card card--back" aria-label="Card back">
    <div class="wordmark"><span class="wordmark__square"></span>Veltrow Drafts</div>
  </section>
</main>
</body>
</html>
```